Website for Ravok Capital

We need a new web design for a company based in Chicago called "Ravok Capital". Ravok provides portfolio management and financial advice using primarily income oriented strategies, such as, dividend paying stocks and preferred stocks. Our niche is utilizing conservative option strategies to help generate income and minimize risk. We are looking for a clean-cut and streamline professional site that is both appealing and user friendly. We would like the main colors to be the dark blue and bright green of our logo. Depending on cost and ease, we may want a designer to give us the completed website, including the coding, etc.

Target Market(s)

20-80 year old affluent investors seeking portfolio management and investment advice.

Industry/Entity Type

Conservative

Requirements
Must have
• -our logo
-main tabs: home, about us, our philosophy, our services, investment strategy, compliance, contact us
-our phone number visible and conveniently placed on each page
Nice to have
• -conveniently placed login button for current clients
-conveniently placed "quick contact" box on home page with spaces for first name, last name, email, phone number, and a blank box for their question or comment
-check us out on Facebook and Twitter logos/buttons
-we like the idea of rotating pictures on top of page, but we aren't sure whether or not we definitely want that
Should not have
• -no trees
-no clocks
-no timers
-no crowns
-no plants

```html
<!DOCTYPE html>
<html lang="en">
<head>
<meta charset="utf-8">
<title>Ravok Capital</title>
<link rel="stylesheet" href="https://fonts.googleapis.com/css2?family=Ubuntu:wght@300;400;500&family=Tinos&family=PT+Sans+Narrow:wght@400;700&display=swap">
<style>
  :root {
    --navy: #1b1f8a;
    --navy-dark: #0c1070;
    --green: #7dc242;
    --green-dark: #6aae33;
    --green-text: #4f9a1f;
    --text: #333;
    --muted: #666;
    --line: #dcdcdc;
    --footer: #f4f4f4;
  }
  html, body { margin: 0; padding: 0; overflow: hidden; background: #fff; }
  .page {
    position: relative; width: 997px; height: 1200px; overflow: hidden;
    font-family: "Ubuntu", sans-serif; color: var(--text);
    border-top: 4px solid var(--navy-dark); box-sizing: border-box;
  }
  .abs { position: absolute; }

  /* header */
  .brand { left: 80px; top: 48px; display: flex; align-items: center; gap: 10px; }
  .brand-mark { width: 28px; height: 28px; background: var(--navy); }
  .brand-name { font-size: 32px; font-weight: 500; color: var(--navy); letter-spacing: 1px; }
  .call { right: 68px; top: 45px; text-align: right; color: var(--navy); }
  .call-label { font-size: 17px; font-weight: 300; line-height: 20px; }
  .call-number { font-size: 24px; font-weight: 400; line-height: 28px; }
  .login { left: 624px; top: 103px; display: flex; gap: 7px; }
  .login input {
    width: 117px; height: 28px; box-sizing: border-box; border: 1px solid #ccc;
    font: 300 11.5px "Ubuntu", sans-serif; padding: 0 8px; color: #888;
  }
  .login input::placeholder { color: #888; }
  .btn {
    background: var(--navy-dark); color: #fff; border: 0; border-radius: 2px;
    font: 700 13px "PT Sans Narrow", sans-serif; letter-spacing: .3px; text-transform: uppercase;
    display: inline-flex; align-items: center; justify-content: center; text-decoration: none;
  }
  .login .btn { width: 58px; height: 29px; margin-left: -3px; }

  /* navigation */
  .nav { left: 55px; top: 144px; width: 886px; height: 47px; background: var(--green); display: flex; }
  .nav a {
    color: #fff; text-decoration: none; font: 15px "Tinos", serif; text-transform: uppercase;
    display: flex; align-items: center; justify-content: center; white-space: nowrap;
    border-right: 1px solid var(--green-dark);
  }
  .nav a:last-child { border-right: 0; }

  /* hero */
  .hero { left: 54px; top: 191px; width: 888px; height: 319px; border: 1px solid #e6e6e6; border-top: 0; box-sizing: border-box; box-shadow: 0 1px 3px rgba(0,0,0,.06); }
  .hero-photo { left: 405px; top: 4px; width: 474px; height: 309px;
    background: linear-gradient(90deg, #ffffff 0%, #e7ebf0 18%, #b9c3cf 45%, #5c6f8a 75%, #23324c 100%); }
  .hero-copy { left: 55px; top: 72px; width: 345px; }
  .hero-kicker { font: 21px "Tinos", serif; color: var(--navy); line-height: 26px; margin: 0; white-space: nowrap; }
  .hero-title { font: 34px "Tinos", serif; color: var(--navy); line-height: 40px; margin: 0; white-space: nowrap; }
  .hero-sub { font: 400 16.5px "Ubuntu", sans-serif; color: var(--green-text); margin: 2px 0 8px; white-space: nowrap; }
  .hero-text { font: 300 11.5px/17px "Ubuntu", sans-serif; color: var(--green-text); margin: 0 0 12px; }
  .hero .btn { width: 90px; height: 27px; }

  /* welcome */
  .welcome { left: 54px; top: 545px; width: 610px; }
  .welcome h1 { font-size: 23px; font-weight: 400; margin: 0 0 8px; color: var(--green); }
  .welcome h1 span { color: var(--navy); font-weight: 500; }
  .welcome .lead { font-size: 13.5px; margin: 0 0 8px; color: #222; }
  .welcome .body { font: 300 11.5px/21px "Ubuntu", sans-serif; color: var(--muted); margin: 0; }

  /* feature columns */
  .feature { top: 725px; width: 192px; height: 290px; }
  .feature h2 { font-size: 17.5px; font-weight: 400; color: var(--navy); margin: 0 0 6px; white-space: nowrap; }
  .feature .thumb { width: 192px; height: 104px; border: 1px solid #ddd; box-sizing: border-box; }
  .feature h3 { font-size: 13px; font-weight: 400; margin: 10px 0 6px; color: #222; }
  .feature p { font: 300 11px/17.4px "Ubuntu", sans-serif; color: var(--muted); margin: 0; }
  .feature ul { list-style: none; padding: 0; margin: 11px 0 0; }
  .feature li { font: 300 11.5px/21.7px "Ubuntu", sans-serif; color: var(--navy); display: flex; align-items: center; gap: 6px; white-space: nowrap; }
  .more { position: absolute; top: 268px; font-size: 11.5px; color: var(--navy); text-decoration: none; display: flex; align-items: center; gap: 4px; }
  .more svg { width: 5px; height: 8px; }

  /* contact form */
  .quick { left: 686px; top: 538px; width: 253px; height: 462px; border: 1px solid #e3e3e3; box-sizing: border-box; }
  .quick-head { height: 45px; background: var(--green); display: flex; align-items: center; justify-content: space-between; padding: 0 22px 0 24px; margin: -1px -1px 0; }
  .quick-head h2 { font-size: 18px; font-weight: 400; color: var(--navy); margin: 0; }
  .field { position: absolute; left: 20px; width: 212px; }
  .field label { display: block; font-size: 12px; font-weight: 300; color: #444; margin-bottom: 3px; }
  .field input, .field textarea { width: 212px; box-sizing: border-box; border: 1px solid #d6d6d6; border-radius: 2px; height: 25px; display: block; }
  .field textarea { height: 99px; resize: none; }
  .quick .btn { position: absolute; left: 20px; top: 413px; width: 89px; height: 26px; }

  /* footer */
  .footer { left: 0; top: 1060px; width: 997px; height: 140px; background: var(--footer); box-shadow: inset 0 5px 6px -3px rgba(0,0,0,.06); }
  .footer-nav { position: absolute; left: 51px; top: 38px; font: 13.5px "PT Sans Narrow", sans-serif; color: #444; white-space: nowrap; }
  .footer-nav a { color: #444; text-decoration: none; text-transform: uppercase; }
  .footer-nav span { margin: 0 6px; }
  .copyright { position: absolute; left: 53px; top: 67px; font: 300 9.5px "Ubuntu", sans-serif; color: #555; }
  .social { position: absolute; left: 859px; top: 38px; display: flex; gap: 4px; }
  .social a { width: 21px; height: 21px; border-radius: 2px; display: block; }
  .social .s1 { background: #3aa6de; } .social .s2 { background: #2573a7; } .social .s3 { background: #3b5998; }
</style>
</head>
<body>
<div class="page">

  <header>
    <div class="abs brand"><span class="brand-mark"></span><span class="brand-name">Ravok Capital</span></div>
    <div class="abs call">
      <div class="call-label">Call Us Now</div>
      <div class="call-number">800.555.0142</div>
    </div>
    <form class="abs login">
      <input type="text" placeholder="Username">
      <input type="password" placeholder="Password">
      <button class="btn" type="button">Login</button>
    </form>
    <nav class="abs nav">
      <a href="#" style="width:81px">Home</a>
      <a href="#" style="width:97px">About Us</a>
      <a href="#" style="width:151px">Our Philosophy</a>
      <a href="#" style="width:126px">Our Services</a>
      <a href="#" style="width:192px">Investment Strategy</a>
      <a href="#" style="width:118px">Compliance</a>
      <a href="#" style="width:121px">Contact Us</a>
    </nav>
  </header>

  <section class="abs hero">
    <div class="abs hero-photo" role="img" aria-label="Photo of an advisor shaking hands with a smiling couple at a meeting table"></div>
    <div class="abs hero-copy">
      <p class="hero-kicker">LOREM IPSUM DOLOR SIT AMET</p>
      <p class="hero-title">INVESTMENT GROUP</p>
      <p class="hero-sub">Mauris vel lacus vitae vestibulum volutpat.</p>
      <p class="hero-text">Mauris vel lacus vitae felis vestibulum volutpat. Etiam est nunc, venenatis in, tristique eu, imperdiet ac, nisl. Cum sociis natoque penatibus et magnis dis parturient montes</p>
      <a class="btn" href="#">Learn More</a>
    </div>
  </section>

  <section class="abs welcome">
    <h1>Welcome to <span>Ravok Capital Mainpage</span></h1>
    <p class="lead">Duis tincidunt lectus quis dui viverra vestibulum. Suspendisse vulputate aliquam dui.</p>
    <p class="body">Nulla elementum dui ut augue. Aliquam vehicula mi at mauris. Maecenas placerat, nisl at consequat rhoncus, sem nunc gravida justo, quis eleifend arcu velit quis lacus. Morbi magna magna, tincidunt a, mattis non, imperdiet vitae, tellus. Sed odio est, auctor ac, sollicitudin in, consequat vitae, orci. Fusce id felis. Vivamus sollicitudin metus eget eros.</p>
  </section>

  <section class="abs feature" style="left:53px">
    <h2>Why We Are</h2>
    <div class="thumb" role="img" aria-label="Illustration of a hand touching a rising blue growth chart with a dollar symbol" style="background:linear-gradient(135deg,#9fd3f5,#2a86d6)"></div>
    <h3>Urabitur vel mi sit amet</h3>
    <p>Magna malesuada ultrices. Ut nisi erat, fermentum vel, congue id, euismod in, elit. Fusce ultricies, orci ac feugiat suscipit, leo massa sodales velit, et scelerisque</p>
    <a class="more" href="#" style="left:1px">Learn More <svg viewBox="0 0 5 8"><path d="M0 0L5 4L0 8Z" fill="currentColor"/></svg></a>
  </section>

  <section class="abs feature" style="left:260px">
    <h2>Investment Strategy</h2>
    <div class="thumb" role="img" aria-label="Photo of hands reviewing printed financial bar charts with a pen" style="background:linear-gradient(135deg,#d9cbbb,#f2f2f2 50%,#6f8fb5)"></div>
    <h3>Urabitur vel mi sit amet</h3>
    <p>Magna malesuada ultrices. Ut nisi erat, fermentum vel, congue id, euismod in, elit. Fusce ultricies, orci ac feugiat suscipit, leo massa sodales velit, et scelerisque</p>
    <a class="more" href="#" style="left:1px">Learn More <svg viewBox="0 0 5 8"><path d="M0 0L5 4L0 8Z" fill="currentColor"/></svg></a>
  </section>

  <section class="abs feature" style="left:469px">
    <h2 style="margin-left:-2px">Services We Provide</h2>
    <div class="thumb" role="img" aria-label="Photo of a hand dropping a coin into a piggy bank" style="background:linear-gradient(135deg,#b7c6da,#e8d9d6 55%,#8fa2bf)"></div>
    <ul>
      <li><svg width="10" height="9" viewBox="0 0 10 9"><path d="M1 5L4 8L9 1" fill="none" stroke="#1b1f8a" stroke-width="2"/></svg>Phasellus felis dolor</li>
      <li><svg width="10" height="9" viewBox="0 0 10 9"><path d="M1 5L4 8L9 1" fill="none" stroke="#1b1f8a" stroke-width="2"/></svg>Scelerisque a tempus eget</li>
      <li><svg width="10" height="9" viewBox="0 0 10 9"><path d="M1 5L4 8L9 1" fill="none" stroke="#1b1f8a" stroke-width="2"/></svg>Lobortis id libero.</li>
      <li><svg width="10" height="9" viewBox="0 0 10 9"><path d="M1 5L4 8L9 1" fill="none" stroke="#1b1f8a" stroke-width="2"/></svg>Donec scelerisque leo</li>
      <li><svg width="10" height="9" viewBox="0 0 10 9"><path d="M1 5L4 8L9 1" fill="none" stroke="#1b1f8a" stroke-width="2"/></svg>Praesent sit amet est.</li>
    </ul>
    <a class="more" href="#" style="left:4px">Learn More <svg viewBox="0 0 5 8"><path d="M0 0L5 4L0 8Z" fill="currentColor"/></svg></a>
  </section>

  <aside class="abs quick">
    <div class="quick-head">
      <h2>Quick Contact Form</h2>
      <svg width="38" height="30" viewBox="0 0 38 30">
        <path d="M3 12L19 2L35 12V28H3Z" fill="#fff"/>
        <path d="M3 12L19 22L35 12" fill="none" stroke="#7dc242" stroke-width="2"/>
        <path d="M3 28L15 19M35 28L23 19" stroke="#7dc242" stroke-width="1.5"/>
      </svg>
    </div>
    <div class="field" style="top:70px"><label>First Name</label><input type="text"></div>
    <div class="field" style="top:129px"><label>Last Name</label><input type="text"></div>
    <div class="field" style="top:181px"><label>Email add</label><input type="email"></div>
    <div class="field" style="top:240px"><label>Phone no.</label><input type="tel"></div>
    <div class="field" style="top:293px"><label>Comments</label><textarea></textarea></div>
    <button class="btn" type="button">Submit Now</button>
  </aside>

  <footer class="abs footer">
    <div class="footer-nav">
      <a href="#">Home</a><span>|</span><a href="#">About Us</a><span>|</span><a href="#">Our Philosophy</a><span>|</span><a href="#">Our Services</a><span>|</span><a href="#">Investment Strategy</a><span>|</span><a href="#">Compliance</a><span>|</span><a href="#">Contact Us</a>
    </div>
    <div class="copyright">Copyright © 2013 Company Name.&nbsp; All right reserved.&nbsp; Term of Use</div>
    <div class="social">
      <a class="s1" href="#" aria-label="Social profile one"></a>
      <a class="s2" href="#" aria-label="Social profile two"></a>
      <a class="s3" href="#" aria-label="Social profile three"></a>
    </div>
  </footer>

</div>
</body>
</html>
```